Gutscheine
Zielgruppe
Immobilienmakler, Verkauf und Vermietung, Immobilienbewertung
Aufgabenstellung
Es soll eine Gutscheinkarte werden für die Verteilung auf einen Stadtfest am Stand vor unserem Büro.
Es soll ein Bezug zu Immobilien haben, aber auch eine Emotion vermitteln. Daher Bild mit Familie oder Rentner. Zielgruppe sollen sein zum einen junge Leute, die vor haben eine Immobilie zu kaufen. Und auf der anderen Seite Leute, die mit dem Gedanken spielen eine Immobilie aus Altersgründen, Trennung, Scheidung oder nach Erbe zu verkaufen. Dominant soll mit dem Gutschein zur kostenlosen Bewertung einer Immobilie gelockt werden.
Auf der Rückseite soll es so sein, dass Kunden ankreuzen können, ob Sie eine Immobilie evtl. Verkaufen möchten und eine kostenlose Bewertung wünschen.
Evtl. macht es Sinn zwei Karten anzulegen. Einmal Zielgruppe Käufer/Suchende, einmal Verkäufer.
Beim Format bin ich flexibel und für alles . Es kann länglich sein, aber auch quadratisch.
Vom Design einen Bezug zu den bisherigen Flyern und Broschüren im Anhang.
Bilder die auf der Homepage sind, sind als Stockbilder vorhanden.
Es werden noch einige andere Sachen für das Stadtfest benötigt. Wie Bierdeckel, Imagebroschüre zum Aufklappen, Banner, Roll-Up, Luftballons.

```html
<!DOCTYPE html>
<html lang="de">
<head>
<meta charset="utf-8">
<title>Rinkel Immobilien – Gutscheinkarten</title>
<link rel="stylesheet" href="https://fonts.googleapis.com/css2?family=Cinzel:wght@500;600&family=Ubuntu:wght@400;500;700&display=swap">
<style>
  :root {
    --navy: #14336a;
    --gold: #c3aa55;
    --gold-soft: rgba(195,170,85,0.55);
    --white: #ffffff;
    --grey-text: #555a60;
    --stage: #6b6b6b;
  }
  * { margin: 0; padding: 0; box-sizing: border-box; }
  html, body { width: 959px; height: 1200px; overflow: hidden; background: var(--stage); }
  body { position: relative; font-family: "Ubuntu", sans-serif; }

  .card { position: absolute; left: 60px; width: 839px; height: 512px; background: var(--white); overflow: hidden; }
  .card--voucher { top: 71px; }
  .card--sell { top: 617px; }

  .abs { position: absolute; }
  .gold-bar { position: absolute; width: 23px; background: var(--gold); }
  .gold-bar--soft { background: var(--gold-soft); }

  /* Front card */
  .voucher-band { left: 0; top: 0; width: 839px; height: 86px; background: var(--navy); }
  .voucher-title { left: 53px; top: 24px; font-family: "Cinzel", serif; font-weight: 500; font-size: 40px; line-height: 40px; color: var(--white); letter-spacing: 0; white-space: nowrap; }
  .voucher-offer { left: 535px; top: 28px; font-weight: 700; font-size: 17px; line-height: 20px; color: var(--white); }

  .photo-family { left: 0; top: 86px; width: 839px; height: 303px;
    background: linear-gradient(90deg, #6e5a48 0%, #b79a80 25%, #c9c2bb 50%, #dfe3e6 75%, #bfc9d2 100%); }

  .brand-panel { left: 327px; top: 0; width: 185px; height: 203px; }
  .brand-square { left: 46px; top: 23px; width: 92px; height: 92px; background: var(--gold); }
  .brand-name { left: 0; width: 185px; top: 120px; text-align: center; font-family: "Cinzel", serif; font-weight: 500; font-size: 38px; color: var(--navy); letter-spacing: 2px; }
  .brand-sub { left: 0; width: 185px; top: 165px; text-align: center; font-size: 9px; letter-spacing: 2px; color: var(--navy); }

  .valuation-question { left: 52px; top: 405px; font-weight: 700; font-size: 16px; color: var(--gold); }
  .valuation-copy { left: 52px; top: 426px; width: 390px; font-size: 14px; line-height: 19.5px; color: var(--grey-text); }

  .call-invite { left: 502px; top: 424px; font-weight: 700; font-size: 18px; color: var(--gold); }
  .call-number { left: 510px; top: 444px; font-weight: 700; font-size: 36px; color: var(--white); }
  .call-icon { left: 473px; top: 454px; }

  /* Back card */
  .sell-title { left: 0; width: 839px; top: 22px; text-align: center; font-family: "Cinzel", serif; font-weight: 500; font-size: 33px; line-height: 38px; color: var(--navy); letter-spacing: 0; white-space: nowrap; }
  .sell-tagline { left: 0; width: 839px; top: 61px; text-align: center; font-weight: 700; font-size: 17px; color: var(--gold); letter-spacing: 0.3px; }
  .photo-house { left: 0; top: 93px; width: 839px; height: 278px;
    background: linear-gradient(180deg, #dfe3e6 0%, #8b8f95 40%, #6d7076 65%, #5f8a3e 88%, #4d7a30 100%); }

  .contact-band { left: 0; top: 371px; width: 839px; height: 141px; background: var(--navy); }
  .contact-call { left: 62px; top: 401px; font-weight: 700; font-size: 21.5px; line-height: 25px; color: var(--white); }
  .contact-divider { left: 332px; top: 393px; width: 2px; height: 96px; background: var(--gold); }
  .contact-info { left: 351px; top: 397px; font-size: 14px; line-height: 16.5px; color: var(--white); }
  .contact-info .firm { font-weight: 700; color: var(--gold); }
  .contact-info .gap { height: 16px; }

  .mini-brand-square { left: 698px; top: 385px; width: 62px; height: 62px; background: var(--gold); }
  .mini-brand-name { left: 670px; width: 118px; top: 456px; text-align: center; font-family: "Cinzel", serif; font-weight: 500; font-size: 24px; color: var(--white); letter-spacing: 1px; }
  .mini-brand-sub { left: 670px; width: 118px; top: 486px; text-align: center; font-size: 6.5px; letter-spacing: 1.5px; color: var(--white); }
</style>
</head>
<body>

<section class="card card--voucher">
  <div class="abs voucher-band"></div>
  <div class="abs photo-family" role="img" aria-label="Foto: lachende Familie mit zwei Kindern auf dem Sofa in einer hellen Wohnung mit Stadtblick"></div>
  <div class="gold-bar" style="left:0;top:0;height:86px"></div>
  <div class="gold-bar" style="right:0;top:0;height:86px"></div>
  <div class="gold-bar gold-bar--soft" style="left:0;top:86px;height:303px"></div>
  <div class="gold-bar gold-bar--soft" style="right:0;top:86px;height:303px"></div>

  <h1 class="abs voucher-title">GUTSCHEIN</h1>
  <p class="abs voucher-offer">eine unverbindliche kostenfreie<br>Bewertung Ihrer Immobilie.</p>

  <div class="abs brand-panel">
    <svg class="abs" width="185" height="203" viewBox="0 0 185 203" style="left:0;top:0">
      <polygon points="0,0 185,0 185,182 92.5,203 0,182" fill="#ffffff"/>
    </svg>
    <div class="abs brand-square"></div>
    <div class="abs brand-name">RINKEL</div>
    <div class="abs brand-sub">IMMOBILIEN</div>
  </div>

  <div class="gold-bar" style="left:0;top:395px;height:104px"></div>
  <svg class="abs" width="839" height="123" viewBox="0 0 839 123" style="left:0;top:389px">
    <polygon points="474,19 839,19 839,110 427,110" fill="#14336a"/>
    <rect x="0" y="110" width="839" height="13" fill="#14336a"/>
  </svg>

  <h2 class="abs valuation-question">Wieviel ist meine Immobilie eigentlich wert?</h2>
  <p class="abs valuation-copy">Sollten auch Sie mit dem Gedanken spielen, sich wohnlich<br>zu verändern, so beraten wir Sie gerne persönlich In<br>einem unverbindlichen Gespräch.</p>

  <p class="abs call-invite">Wir freuen uns auf Ihren Anruf!</p>
  <svg class="abs call-icon" width="28" height="28" viewBox="0 0 24 24" aria-hidden="true">
    <path fill="#c3aa55" d="M6.6 10.8c1.4 2.8 3.8 5.1 6.6 6.6l2.2-2.2c.3-.3.7-.4 1-.2 1.1.4 2.3.6 3.6.6.6 0 1 .4 1 1V20c0 .6-.4 1-1 1C10.6 21 3 13.4 3 4c0-.6.4-1 1-1h3.5c.6 0 1 .4 1 1 0 1.3.2 2.5.6 3.6.1.3 0 .7-.2 1l-2.3 2.2z"/>
  </svg>
  <p class="abs call-number">02242. 47 31 608</p>
</section>

<section class="card card--sell">
  <div class="gold-bar" style="left:0;top:0;height:87px"></div>
  <div class="gold-bar" style="right:0;top:0;height:87px"></div>
  <h1 class="abs sell-title">MÖCHTEN SIE IMMOBILIEN VERKAUFEN?</h1>
  <p class="abs sell-tagline">Unsere Leidenschaft für Ihre Immobilie.</p>

  <div class="abs photo-house" role="img" aria-label="Foto: modernes Einfamilienhaus mit Doppelgarage, beleuchteten Fenstern und Vorgarten"></div>
  <div class="gold-bar gold-bar--soft" style="left:0;top:93px;height:278px"></div>
  <div class="gold-bar gold-bar--soft" style="right:0;top:93px;height:278px"></div>

  <div class="abs contact-band"></div>
  <div class="gold-bar" style="left:0;top:377px;height:135px"></div>
  <div class="gold-bar" style="right:0;top:377px;height:135px"></div>

  <p class="abs contact-call">KONTAKTIEREN SIE UNS<br>FÜR EINE KOSTENLOSE<br>BEWERTUNG</p>
  <div class="abs contact-divider"></div>
  <div class="abs contact-info">
    <div class="firm">RINKEL IMMOBILIEN – seit 2009</div>
    <div>Ihre Maklerin in Bergheim und Umgebung</div>
    <div>kontakt@rinkelimmobilien.de | rinkelimmobilien.de</div>
    <div class="gap"></div>
    <div>Marlene Rinkel | Kauffrau der Grundstücks-</div>
    <div>und Wohnungswirtschaft (IHK)</div>
  </div>

  <div class="abs mini-brand-square"></div>
  <div class="abs mini-brand-name">RINKEL</div>
  <div class="abs mini-brand-sub">IMMOBILIEN</div>
</section>

</body>
</html>
```